International business needs business cards

Our company, DOR Ventures Inc. is in the business of supplying a range construction products with particular emphasis on CEMENT. We have developed our own brand - BRUNVALE MATERIALS - with which to infiltrate the market. We are launching our brand of cement (BRUNVALE Type IS Cement) into the Caribbean which is unlike anything this market has ever seen. A monopoly has existed here for the past 60-odd years and the market has now opened to allow the importation of other brands and consumers are anxious and ready for change/improvement. We are very excited to be launching and want to make a great first impression. We will be conducting workshops and seminars (from government level to the hardware store owners) and we want our business card to give us the strong, confident introduction that we need.

Target Market(s)

construction; builders; engineers; home owners

Industry/Entity Type

Construction

Contact Information for Business Card

Marisol Penwick
CEO
cell # 1 555 4817730
Ground floor,Lantern Plaza Suite 2483
George Town,Grand Cayman
Cayman Islands,KY1-2250
EMAIL: m.penwick@dorventuresinc.example
web site dorventuresinc.example

COMPANY: skype info dor.ventures.example

second card
Tamsin Rowe-Penwick
CFO
CELL# 1 555 604 3917
George Town,Grand Cayman
Cayman Islands,KY1-2250
EMAIL: t.rowepenwick@dorventuresinc.example
website dorventuresinc.example

Requirements
Must have
• Business cards must display BOTH logos - DOR is the company and BRUNVALE is the brand.

```html
<!DOCTYPE html>
<html lang="en">
<head>
<meta charset="utf-8">
<title>DOR Ventures Inc. — Business Card</title>
<link rel="stylesheet" href="https://fonts.googleapis.com/css2?family=Open+Sans:wght@400;600;700&display=swap">
<style>
  :root {
    --page: #e8e5e0;
    --card-white: #f4f4f4;
    --card-grey: #dcdcdc;
    --red: #b01f26;
    --red-dark: #8e161c;
    --black: #141414;
    --ink: #1c1c1c;
    --white: #ffffff;
    --icon-grey: #b9c3cf;
  }
  * { margin: 0; padding: 0; box-sizing: border-box; }
  html, body { width: 1200px; height: 780px; overflow: hidden; }
  body {
    background: var(--page);
    font-family: "Open Sans", Arial, sans-serif;
    position: relative;
  }
  .card {
    position: absolute;
    top: 233px;
    width: 550px;
    height: 314px;
    border-radius: 16px;
    overflow: hidden;
    box-shadow: 0 6px 18px rgba(0,0,0,0.18);
  }
  .card-front { left: 30px; background: var(--card-white); }
  .card-back {
    left: 620px;
    background: radial-gradient(ellipse at 50% 50%, var(--white) 0%, var(--card-white) 45%, var(--card-grey) 100%);
  }
  .front-art { position: absolute; inset: 0; width: 100%; height: 100%; }

  .company-mark {
    position: absolute; left: 26px; top: 112px;
    display: flex; align-items: center; gap: 10px;
  }
  .company-mark__square { width: 34px; height: 34px; background: var(--red); }
  .company-mark__name {
    font-weight: 700; font-size: 23px; color: var(--ink); letter-spacing: -0.2px;
  }

  .social-spots { position: absolute; left: 352px; top: 14px; display: flex; gap: 8px; }
  .social-spots span { width: 20px; height: 20px; border-radius: 50%; background: var(--icon-grey); }

  .website {
    position: absolute; right: 24px; top: 108px;
    color: var(--white); font-size: 14px;
  }

  .person { position: absolute; left: 252px; top: 182px; color: var(--white); }
  .person__name { font-weight: 700; font-size: 22px; line-height: 1.1; }
  .person__role { font-size: 13px; margin-bottom: 12px; }
  .contact-line { display: flex; align-items: center; gap: 7px; font-size: 13.5px; line-height: 1.75; }
  .contact-line svg { width: 14px; height: 14px; flex: none; }

  .address {
    position: absolute; left: 28px; top: 24px;
    font-size: 14px; line-height: 1.5; color: var(--ink);
  }
  .address__second { padding-left: 70px; }

  .brand-mark {
    position: absolute; left: 0; right: 0; top: 150px;
    display: flex; justify-content: center; align-items: center; gap: 12px;
  }
  .brand-mark__circle { width: 30px; height: 30px; border-radius: 50%; background: #555; }
  .brand-mark__name { font-weight: 700; font-size: 24px; color: #3a3a3a; letter-spacing: 1px; }
</style>
</head>
<body>

  <section class="card card-front" aria-label="Business card front">
    <svg class="front-art" viewBox="0 0 550 314" preserveAspectRatio="none" aria-hidden="true">
      <defs>
        <linearGradient id="redBand" x1="0" y1="1" x2="1" y2="0">
          <stop offset="0" stop-color="#a81b22"/>
          <stop offset="1" stop-color="#c3252c"/>
        </linearGradient>
      </defs>
      <path class="wave-black" d="M 112 314 C 212 290, 242 160, 312 100 S 402 10, 422 0 L 550 0 L 550 314 Z" fill="#141414"/>
      <path class="wave-red" d="M 130 314 C 230 290, 260 160, 330 100 S 420 10, 440 0 L 550 0 L 550 314 Z" fill="url(#redBand)"/>
    </svg>

    <div class="company-mark">
      <span class="company-mark__square"></span>
      <span class="company-mark__name">DOR Ventures Inc.</span>
    </div>

    <div class="social-spots" aria-hidden="true"><span></span><span></span></div>

    <div class="website">dorventuresinc.example</div>

    <div class="person">
      <div class="person__name">Marisol Penwick</div>
      <div class="person__role">CEO</div>
      <div class="contact-line">
        <svg viewBox="0 0 14 14" aria-hidden="true"><rect width="14" height="14" rx="2" fill="#fff"/><path d="M4 3.2 L5.6 3 L6.3 5 L5.3 5.8 C5.8 7 6.8 8 8 8.6 L8.8 7.6 L10.8 8.3 L10.6 9.9 C7 10.3 3.7 7 4 3.2 Z" fill="#b01f26"/></svg>
        <span>1 555 4817730</span>
      </div>
      <div class="contact-line">
        <svg viewBox="0 0 14 14" aria-hidden="true"><rect width="14" height="14" rx="2" fill="#fff"/><rect x="3" y="4" width="8" height="6" fill="none" stroke="#b01f26" stroke-width="1.2"/><path d="M3 4 L7 7.5 L11 4" fill="none" stroke="#b01f26" stroke-width="1.2"/></svg>
        <span>m.penwick@dorventuresinc.example</span>
      </div>
    </div>
  </section>

  <section class="card card-back" aria-label="Business card back">
    <div class="address">
      <div>Ground floor,Lantern Plaza Suite 2483, George Town,Grand Cayman</div>
      <div class="address__second">Cayman Islands,KY1-2250</div>
    </div>
    <div class="brand-mark">
      <span class="brand-mark__circle"></span>
      <span class="brand-mark__name">BRUNVALE MATERIALS</span>
    </div>
  </section>

</body>
</html>
```